KLMR stationery 2023

Our stationery dates back to 2007 when we changed practice rooms.
We would like to have kept the logo and spiced up the design, especially since we have one more colleague (Dr. Henriette Bollmeyer)
Our practice colors are a slightly more muted pink and sand-colored.
Follow-up orders for flyers, notices, etc. are still waiting for this design.

```html
<!DOCTYPE html>
<html lang="de">
<head>
<meta charset="utf-8">
<title>KLMR Briefpapier</title>
<link href="https://fonts.googleapis.com/css2?family=Roboto+Condensed:ital,wght@0,400;0,700;1,700&display=swap" rel="stylesheet">
<style>
  :root {
    --rose: #c0678f;
    --rose-soft: #dfa9c1;
    --rose-pale: #f6e4ec;
    --sand: #cdb48c;
    --sand-light: #efe5d3;
    --sand-pale: #f8f3ea;
    --ink: #4a4340;
    --paper: #ffffff;
  }
  html, body {
    margin: 0;
    padding: 0;
    overflow: hidden;
    background: var(--paper);
  }
  .sheet {
    position: relative;
    width: 849px;
    height: 1200px;
    overflow: hidden;
    background: var(--paper);
    font-family: "Roboto Condensed", Arial, sans-serif;
    color: var(--ink);
  }
  .brand {
    position: absolute;
    top: 40px;
    left: 0;
    width: 849px;
    text-align: center;
    font-size: 58px;
    font-weight: 700;
    letter-spacing: 4px;
    color: var(--rose);
    line-height: 1;
  }
  .doctor-bar {
    position: absolute;
    top: 114px;
    left: 0;
    width: 849px;
    height: 28px;
    border-top: 2px solid var(--rose);
    border-bottom: 2px solid var(--sand);
    background: var(--sand-pale);
    display: flex;
    justify-content: center;
    align-items: center;
    gap: 18px;
    font-size: 13px;
  }
  .doctor::before {
    content: "";
    display: inline-block;
    width: 6px;
    height: 6px;
    margin-right: 6px;
    background: var(--sand);
    vertical-align: middle;
  }
  .artwork {
    position: absolute;
    left: 50px;
    top: 940px;
    width: 240px;
    height: 180px;
    background: linear-gradient(160deg, var(--sand-light) 0%, var(--rose-pale) 45%, var(--rose-soft) 100%);
  }
  .footer-brand {
    position: absolute;
    left: 304px;
    top: 1084px;
    font-size: 24px;
    font-weight: 700;
    letter-spacing: 1px;
    color: var(--rose);
    line-height: 1;
  }
  .contact {
    position: absolute;
    top: 1084px;
    font-size: 10.5px;
    line-height: 14px;
    margin: 0;
    padding-left: 8px;
    border-left: 2px solid var(--sand);
  }
  .contact-address { left: 400px; }
  .contact-phone { left: 515px; }
  .contact-web { left: 640px; }
  .hours-rule {
    position: absolute;
    left: 0;
    top: 1122px;
    width: 849px;
    height: 4px;
    background: var(--sand);
  }
  .hours-band {
    position: absolute;
    left: 0;
    top: 1126px;
    width: 849px;
    height: 40px;
    background: var(--rose);
    display: flex;
    align-items: center;
    justify-content: center;
    color: var(--paper);
    font-size: 22px;
    font-weight: 700;
    font-style: italic;
    letter-spacing: 0.3px;
  }
</style>
</head>
<body>
<div class="sheet">
  <header>
    <div class="brand">KLMR</div>
    <nav class="doctor-bar">
      <span class="doctor">Dr. Gudrun Lindqvist</span>
      <span class="doctor">Dr. Petra Sommerau</span>
      <span class="doctor">Dr. Matthias Lindqvist</span>
      <span class="doctor">Dr. Ilona Berczi</span>
      <span class="doctor">Dr. Henriette Bollmeyer</span>
    </nav>
  </header>

  <footer>
    <div class="artwork" role="img" aria-label="Line illustration of running women in front of the practice building"></div>
    <div class="footer-brand">KLMR</div>
    <p class="contact contact-address">Kastanienweg 14<br>8400 Musterdorf</p>
    <p class="contact contact-phone">Tel 052 000 11 22<br>Fax 052 000 11 23</p>
    <p class="contact contact-web">praxis@klmr-aerztinnen.ch<br>www.klmr-aerztinnen.ch</p>
    <div class="hours-rule"></div>
    <div class="hours-band">Öffnungszeiten NEU:&nbsp; Montag - Freitag 08.00 - 12.00 Uhr&nbsp; und&nbsp; 13.00 - 17.00 Uhr</div>
  </footer>
</div>
</body>
</html>
```